New Professional Business Web Site

We need a web design for an existing company based in Dallas called "FinchLoop".
We provide software and professional services to enterprise customers in the contact centre space. We have a global customer base but primarily US and UK.
Our initial products are as follows-
LineSight - an application that helps Torvane contact centre managers and administrators observe individual calls in queue.
MassLoad - an application that allows Torvane administrators to load large groups of extensions and associate them to places.
ClustR - an application that helps Torvane customers manage multilayers of agent and place groups into hiearchical and geographical groups of groups.
We would like to see designs that use the colors black, gray, and red as this matches with our new logo we have had designed from this web site and will have available in a few days.
The final design should communicate professionalism, innovation, software, large corporation, and telecommunications.
We're looking to provide features like-
1) Interactive Support Portal for customers
2) Product Descriptions
3) Product Purchasing
4) Interactive Forum
Target Market(s)
enterprise companies interested in call center related products and services
Industry/Entity Type
Business
Look and feel

```html
<!DOCTYPE html>
<html lang="en">
<head>
<meta charset="utf-8">
<title>FinchLoop – Contact Centre Software</title>
<link href="https://fonts.googleapis.com/css2?family=Arimo:wght@400;700&family=PT+Sans:wght@400;700&display=swap" rel="stylesheet">
<style>
:root{
  --black:#000;
  --red:#b80c10;
  --red-dark:#8e0508;
  --red-text:#b30d0d;
  --white:#fff;
  --grey-text:#9a9a9a;
  --grey-line:#d6d6d6;
  --ink:#111;
  --link:#1a4f9c;
  --trial-bg:#fdfde6;
  --trial-line:#e2e2c8;
}
*{margin:0;padding:0;box-sizing:border-box}
html,body{width:1099px;height:1200px;overflow:hidden;background:var(--white)}
body{position:relative;font-family:"Arimo",Arial,sans-serif;color:var(--ink)}
.abs{position:absolute;white-space:nowrap}

/* header */
.site-header{left:0;top:0;width:1099px;height:139px;background:radial-gradient(ellipse 260px 160px at 120px 40px,#3a3a3a,var(--black) 75%),var(--black)}
.brand{left:40px;top:52px;display:flex;align-items:center;gap:12px}
.brand-dot{width:30px;height:30px;border-radius:50%;background:var(--red)}
.brand-name{font-family:"PT Sans",sans-serif;font-weight:700;font-size:46px;color:#8d8d8d;line-height:1}
.say-hello{left:633px;top:22px;font-size:13px;color:var(--grey-text)}
.phone{left:713px;top:19px;font-size:16px;color:var(--white)}
.get-intouch{left:860px;top:22px;font-size:13px;color:var(--grey-text)}
.social{display:flex;gap:10px}
.social span{width:19px;height:19px;border-radius:50%;background:#8a8a8a;display:block}
.top-social{left:966px;top:16px}
.main-nav a{position:absolute;white-space:nowrap;top:77px;height:33px;line-height:33px;font-size:13px;color:var(--white);text-decoration:none}
.main-nav .current{background:var(--red);border-radius:6px;padding:0 10px}

/* hero */
.hero{left:16px;top:139px;width:1069px;height:384px;background:radial-gradient(circle 380px at 760px 60px,#d2151a,var(--red) 60%,#a80a0e);border-radius:4px 4px 0 0;overflow:hidden}
.hero-title{left:40px;top:70px;font-family:"PT Sans",sans-serif;font-weight:400;font-size:48px;color:var(--white);letter-spacing:-.5px}
.hero-text{left:41px;top:146px;width:365px;white-space:normal;font-family:"PT Sans",sans-serif;font-size:19px;line-height:23px;color:var(--white)}
.btn-learn{left:40px;top:251px;width:163px;height:50px;border-radius:4px;background:linear-gradient(#3a3a3a,#000);border:3px solid var(--red-dark);color:var(--white);font-weight:700;font-size:15px;text-align:center;line-height:44px;text-decoration:none}
.hero-shot{left:486px;top:41px;width:550px;height:343px;border-radius:10px 10px 0 0;background:linear-gradient(180deg,#e4e4e4,#f7f7f7 30%,#ffffff)}

/* product tabs */
.product-tabs{left:16px;top:523px;width:1069px;height:67px;display:flex;border-bottom:1px solid var(--grey-line);background:var(--white)}
.product-tabs div{font-family:"PT Sans",sans-serif;font-size:20px;text-align:center;line-height:66px;color:var(--ink);border-left:1px solid var(--grey-line)}
.product-tabs .active{background:var(--red);color:var(--white);border-left:none}

/* features */
.section-title{font-weight:400;font-size:31px;color:var(--ink);letter-spacing:-.5px}
.features-title{left:53px;top:636px}
.features-box{left:35px;top:673px;width:341px;height:373px;border:1px solid var(--grey-line);border-radius:6px}
.feature{left:64px;width:300px;display:flex;gap:18px}
.feature-icon{width:60px;height:54px;border-radius:6px;flex:none}
.feature h3{font-weight:400;font-size:19px;color:var(--red-text);margin-bottom:3px}
.feature p{font-size:13.5px;line-height:16px;white-space:normal}

/* welcome */
.welcome-title{left:445px;top:636px}
.welcome-text{left:451px;top:677px;width:575px;white-space:normal;font-size:15px;line-height:23.5px}
.link{color:var(--link);font-size:12px;text-decoration:none}
.welcome-link{left:451px;top:828px}

/* trial */
.trial{left:422px;top:875px;width:629px;height:171px;background:var(--trial-bg);border:1px solid var(--trial-line);border-radius:10px}
.trial-title{left:24px;top:17px}
.trial-text{left:27px;top:66px;width:300px;white-space:normal;font-size:12.5px;line-height:15px}
.trial-art{left:396px;top:22px;width:184px;height:118px;border-radius:50% 20% 20% 50%;background:radial-gradient(circle at 30% 55%,#d4d4d4,#a9a9a9 35%,rgba(41,110,200,.85) 60%,rgba(255,255,255,0) 80%)}

/* footer */
.site-footer{left:0;top:1083px;width:1099px;height:117px;background:var(--black)}
.footer-nav{left:36px;top:35px;display:flex;gap:24px;font-size:11.5px;color:var(--grey-text)}
.footer-nav .current{color:var(--white)}
.copyright{left:36px;top:58px;font-size:12px;color:var(--grey-text)}
.copyright b{color:var(--white);font-weight:400}
.footer-intouch{left:888px;top:58px;font-size:13px;color:var(--white)}
.footer-social{left:966px;top:54px}
</style>
</head>
<body>

<header class="site-header abs">
  <div class="brand abs"><span class="brand-dot"></span><span class="brand-name">FinchLoop</span></div>
  <span class="say-hello abs">SAY HELLO</span>
  <span class="phone abs">+1 214 555 0178</span>
  <span class="get-intouch abs">GET INTOUCH</span>
  <div class="social top-social abs" role="img" aria-label="Social network links"><span></span><span></span><span></span></div>
  <nav class="main-nav">
    <a class="current" href="#" style="left:404px">HOME</a>
    <a href="#" style="left:489px">WHAT WE DO</a>
    <a href="#" style="left:608px">ABOUT US</a>
    <a href="#" style="left:704px">PRODUCTS</a>
    <a href="#" style="left:808px">SERVICES</a>
    <a href="#" style="left:904px">BENEFITS</a>
    <a href="#" style="left:1002px">CONTACT US</a>
  </nav>
</header>

<section class="hero abs">
  <h1 class="hero-title abs">LineSight</h1>
  <p class="hero-text abs">an application that helps Torvane contact centre managers and administrators observe individual calls in queue.</p>
  <a class="btn-learn abs" href="#">LEARN MORE</a>
  <div class="hero-shot abs" role="img" aria-label="Application screenshot on desktop and phone showing a project task list and Gantt chart"></div>
</section>

<div class="product-tabs abs">
  <div class="active" style="width:253px">LineSight</div>
  <div style="width:233px">MassLoad</div>
  <div style="width:291px">ClustR</div>
  <div style="width:292px">Product Four</div>
</div>

<h2 class="section-title features-title abs">Great Features</h2>
<div class="features-box abs"></div>
<div class="feature abs" style="top:710px">
  <div class="feature-icon" role="img" aria-label="Software boxes icon" style="background:linear-gradient(135deg,#b02020,#4a7a2a)"></div>
  <div><h3>Product Descriptions</h3><p>We provide software and proWe provide softwa contact centre</p></div>
</div>
<div class="feature abs" style="top:795px">
  <div class="feature-icon" role="img" aria-label="Support staff with headsets icon" style="background:linear-gradient(135deg,#9aa3ad,#3d4650)"></div>
  <div><h3>Interactive Support</h3><p>We provide software and proWe provide softwa contact centre</p></div>
</div>
<div class="feature abs" style="top:889px">
  <div class="feature-icon" role="img" aria-label="Shopping bag icon" style="background:linear-gradient(135deg,#5a7fa8,#1e3550)"></div>
  <div><h3>Product Purchasing</h3><p>We provide software and proWe provide softwa contact centre</p></div>
</div>
<div class="feature abs" style="top:969px">
  <div class="feature-icon" role="img" aria-label="Forum users icon" style="background:linear-gradient(135deg,#e0a868,#5f9a4a)"></div>
  <div><h3>Interactive Forum</h3><p>We provide software and proWe provide softwa contact centre</p></div>
</div>

<h2 class="section-title welcome-title abs">Welcome to FinchLoop</h2>
<p class="welcome-text abs">We provide software and professional services to enterprise customers in the contact centre space. We have a global customer base but primarily US and UK. We provide software and professional services to enterprise customers in the contact centre space. We have a global customer base but primarily US and UK.We provide software and professional services to enterprise customers in the contact centre space. We have a global customer base but primarily US and UK.</p>
<a class="link welcome-link abs" href="#">Learn More</a>

<section class="trial abs">
  <h2 class="section-title trial-title abs">Get Free Trial Versions</h2>
  <p class="trial-text abs">We provide software and proWe provide softwa cntact centreWWe provide software and proWe provide softwa cntact centreWe provide software and proWe provide softwa cntact centreW &nbsp;<a class="link" href="#">Learn More</a></p>
  <div class="trial-art abs" role="img" aria-label="Stopwatch with a blue check mark"></div>
</section>

<footer class="site-footer abs">
  <nav class="footer-nav abs">
    <span class="current">HOME</span><span>WHAT WE DO</span><span>ABOUT US</span><span>PRODUCTS</span><span>SERVICES</span><span>BENEFITS</span><span>CONTACT US</span>
  </nav>
  <p class="copyright abs">Copyright <b>FINCHLOOP</b>, All Rights Reserved</p>
  <p class="footer-intouch abs">Get intouch</p>
  <div class="social footer-social abs" role="img" aria-label="Social network links"><span></span><span></span><span></span></div>
</footer>

</body>
</html>
```